Postcard Design

New property management company. We manage vacation rental properties on a gulf coast island. This post card will be designed to attract home owners to sign on with us to manage their property (s). We want to convay the message that we will take care if everything needed to maintain value in their investment property to attracting the right sort of renters as well as take care of accounting. We can do this because of our sister relationship with a local contractor and the fact that we are a small company planning to stay that way.
We would like to have a call to action offer of "reduced rates for new clients this month". Please fill free to play with those words. Make is snassy!
Updates

We have some good submissions. I am not sure we have found the "one" yet. We would like some work done with our "reduced rates" phrase. Try different words. It needs to be the most notices sentence. With our phone number being the second line that pops out. Please don't use paragraphs from out website. Phrases are fine. Thank you for your hard work. We look forward to seeing more designs.

Thank you all for your submissions. I appreciate your time.

Target Market(s)

Investment Property Owners from all over Texas, California, Colorado and most Southern States. Usually med to upper income and 35 +

Industry/Entity Type

Property Management

Requirements
Must have
• Catch line " relax- we'll take care of it"
Offer

Our Logo and information

Front and back small post card with return address in left corner and room for mailing label.
Nice to have
• Eye catching!

Noticeable offer

```html
<!DOCTYPE html>
<html lang="en">
<head>
<meta charset="utf-8">
<title>Driftwood Rentals – Postcard</title>
<link rel="stylesheet" href="https://fonts.googleapis.com/css2?family=Architects+Daughter&family=Open+Sans:wght@400;600;700&display=swap">
<style>
  :root {
    --ink: #0d0d0d;
    --royal: #1f2f9c;
    --white: #ffffff;
    --red: #e0261c;
    --sky-top: #5f9ee0;
    --sky-mid: #cfe3f4;
    --grass: #5fbf2a;
    --stage: #6a4a30;
  }
  * { box-sizing: border-box; margin: 0; padding: 0; }
  html, body { width: 1200px; height: 467px; overflow: hidden; }
  body { background: var(--stage); position: relative; font-family: "Open Sans", Arial, sans-serif; }

  .card { position: absolute; top: 17px; width: 552px; height: 427px; overflow: hidden; }
  .card--front { left: 39px; background: var(--ink); }
  .card--back { left: 614px; background: var(--white); }

  /* Front */
  .offer-band { position: absolute; left: 0; top: 0; width: 345px; height: 104px; background: var(--royal);
    clip-path: polygon(0 0, 100% 0, 255px 100%, 0 100%); }
  .offer-headline { position: absolute; left: 12px; top: 6px; color: var(--white); font-weight: 400;
    font-family: "Architects Daughter", cursive; font-size: 26px; line-height: 31px; text-transform: uppercase; letter-spacing: 0.5px; white-space: nowrap; }
  .brand { position: absolute; right: 16px; top: 36px; width: 240px; display: flex; align-items: center; gap: 10px; }
  .brand__dot { width: 16px; height: 16px; border-radius: 50%; background: var(--white); flex: none; }
  .brand__name { color: var(--white); font-weight: 600; font-size: 15px; line-height: 20px; }
  .phone-row { position: absolute; left: 12px; top: 110px; display: flex; align-items: center; gap: 8px;
    color: var(--white); font-weight: 700; font-size: 23px; line-height: 28px; }
  .phone-row svg { width: 22px; height: 22px; }
  .hero { position: absolute; left: 0; top: 142px; width: 552px; height: 253px;
    background: linear-gradient(180deg, var(--sky-top) 0%, var(--sky-mid) 70%, var(--grass) 92%, var(--grass) 100%); }
  .catchline { position: absolute; left: 0; right: 0; top: 244px; text-align: center; color: var(--royal);
    font-family: "Architects Daughter", cursive; font-size: 31px; line-height: 34px; text-transform: uppercase; }
  .web-row { position: absolute; left: 0; right: 0; bottom: 0; height: 32px; display: flex; align-items: center; justify-content: center;
    gap: 8px; color: var(--white); font-size: 19px; }
  .web-row svg { width: 20px; height: 20px; }

  /* Back */
  .message-band { position: absolute; left: 0; top: 0; width: 346px; height: 106px; background: var(--royal);
    clip-path: polygon(0 0, 100% 0, 256px 100%, 0 100%); }
  .message { position: absolute; left: 12px; top: 16px; color: var(--white); font-size: 13px; line-height: 19.5px;
    letter-spacing: 0.2px; white-space: nowrap; }
  .back-phone-band { position: absolute; left: 0; top: 106px; width: 256px; height: 37px; background: var(--ink);
    clip-path: polygon(0 0, 100% 0, 224px 100%, 0 100%); }
  .back-phone { position: absolute; left: 12px; top: 110px; display: flex; align-items: center; gap: 8px;
    color: var(--white); font-weight: 700; font-size: 22px; line-height: 28px; }
  .back-phone svg { width: 21px; height: 21px; }
  .indicia { position: absolute; left: 435px; top: 28px; width: 85px; height: 80px; border: 1px solid #999;
    font-size: 10px; line-height: 13px; text-align: center; padding-top: 7px; color: #222; }
  .mail-label { position: absolute; left: 403px; top: 122px; width: 118px; height: 46px; border: 1px solid #999;
    font-size: 10px; line-height: 13px; padding: 8px 12px; color: #222; }
  .back-brand { position: absolute; left: 16px; top: 278px; display: flex; align-items: center; gap: 8px; }
  .back-brand__dot { width: 14px; height: 14px; border-radius: 50%; background: var(--red); flex: none; }
  .back-brand__name { color: var(--red); font-weight: 600; font-size: 14px; line-height: 18px; }
  .return-address { position: absolute; left: 16px; top: 336px; display: flex; gap: 7px; font-weight: 600; font-size: 12.5px; line-height: 15px; color: var(--ink); }
  .return-address svg { width: 11px; height: 11px; margin-top: 2px; flex: none; }
  .contacts { position: absolute; left: 16px; top: 369px; display: flex; gap: 16px; font-size: 12.5px; line-height: 16px; color: var(--ink); }
  .contacts span { display: flex; align-items: center; gap: 6px; }
  .contacts svg { width: 12px; height: 12px; }
  .back-footer { position: absolute; left: 0; right: 0; bottom: 0; height: 32px; background: var(--ink);
    display: flex; align-items: center; gap: 8px; padding-left: 16px; color: var(--white); font-size: 12.5px; }
  .back-footer svg { width: 15px; height: 15px; }
</style>
</head>
<body>

<section class="card card--front">
  <div class="offer-band"></div>
  <h1 class="offer-headline">Reduced Rates For<br>New Clients<br>This Month</h1>
  <div class="brand">
    <span class="brand__dot"></span>
    <span class="brand__name">Driftwood Rentals and<br>Management Company</span>
  </div>
  <div class="phone-row">
    <svg viewBox="0 0 24 24"><circle cx="12" cy="12" r="10.5" fill="none" stroke="#fff" stroke-width="2"/><path d="M9 6.5c-1.5 1-2 3-1 5.5s3 4.8 5.5 5.6c1.2.4 2.3 0 3-1l-2-2-1.5.8c-1.3-.6-2.6-2-3.2-3.4l.9-1.4-1.7-2.1z" fill="#fff"/></svg>
    <span>361-555-0142</span>
  </div>
  <div class="hero" role="img" aria-label="Photo of two hands forming a roof shape against a blue cloudy sky above green grass with small houses"></div>
  <p class="catchline">Relax<br>We’ll<br>Take Care<br>Of It</p>
  <div class="web-row">
    <svg viewBox="0 0 24 24" fill="none" stroke="#fff" stroke-width="1.8"><circle cx="12" cy="12" r="10"/><ellipse cx="12" cy="12" rx="4.5" ry="10"/><path d="M2 12h20M4 7h16M4 17h16"/></svg>
    <span>driftwoodrentalsisle.com</span>
  </div>
</section>

<section class="card card--back">
  <div class="message-band"></div>
  <p class="message">We will take care if everything needed to<br>maintain value in their investment property<br>to attracting the right sort of renters<br>as well as take care of accounting.</p>
  <div class="back-phone-band"></div>
  <div class="back-phone">
    <svg viewBox="0 0 24 24"><circle cx="12" cy="12" r="10.5" fill="none" stroke="#fff" stroke-width="2"/><path d="M9 6.5c-1.5 1-2 3-1 5.5s3 4.8 5.5 5.6c1.2.4 2.3 0 3-1l-2-2-1.5.8c-1.3-.6-2.6-2-3.2-3.4l.9-1.4-1.7-2.1z" fill="#fff"/></svg>
    <span>361-555-0142</span>
  </div>
  <div class="indicia">PRSRT STD<br>ECRWSS<br>U.S. POSTAGE<br>PAID<br>EDDM Retail</div>
  <div class="mail-label">Local<br>Postal Customer</div>
  <div class="back-brand">
    <span class="back-brand__dot"></span>
    <span class="back-brand__name">Driftwood Rentals and<br>Management Company</span>
  </div>
  <div class="return-address">
    <svg viewBox="0 0 12 12"><path d="M1 6 6 1l5 5v5H1z" fill="#e0261c"/></svg>
    <span>Street Name City Name<br>State Zip Code</span>
  </div>
  <div class="contacts">
    <span><svg viewBox="0 0 24 24"><circle cx="12" cy="12" r="10.5" fill="none" stroke="#e0261c" stroke-width="2.5"/><path d="M9 6.5c-1.5 1-2 3-1 5.5s3 4.8 5.5 5.6c1.2.4 2.3 0 3-1l-2-2-1.5.8c-1.3-.6-2.6-2-3.2-3.4l.9-1.4-1.7-2.1z" fill="#e0261c"/></svg>361-555-0142</span>
    <span><svg viewBox="0 0 24 24"><rect x="2" y="5" width="20" height="14" fill="#e0261c"/><path d="M2 5l10 8 10-8" fill="none" stroke="#fff" stroke-width="1.6"/></svg>hello@driftwoodrentalsisle.com</span>
  </div>
  <div class="back-footer">
    <svg viewBox="0 0 24 24"><circle cx="12" cy="12" r="11" fill="#e0261c"/><g fill="none" stroke="#000" stroke-width="1.4"><ellipse cx="12" cy="12" rx="4.5" ry="10"/><path d="M2 12h20M4 7h16M4 17h16"/></g></svg>
    <span>driftwoodrentalsisle.com</span>
  </div>
</section>

</body>
</html>
```